Kindle Book Cover for Teen Financial Niche

Had a temporary cover done for the book but it needs a lot better cover now it is starting to get some traction.
The current book can be seen here:
https://www.bookvalemart.com/dp/Q7K42LZ9RT
I am wanting something very different if possible. Please search books in the teen financial niche on Bookvale and you will see that a lot of the covers are very similar in style.
I am looking for something different that will stand out in a crowded marketplace.
If you are putting someone on the cover please use a male character rather than a female one.
Thanks
Dale

```html
<!DOCTYPE html>
<html lang="en">
<head>
<meta charset="utf-8">
<title>Personal Finance – Book Cover</title>
<link rel="stylesheet" href="https://fonts.googleapis.com/css2?family=Rubik+Dirt&family=Barlow+Condensed:wght@500;700&display=swap">
<style>
  :root {
    --page: #ffffff;
    --navy: #1c2b5f;
    --navy-deep: #16234f;
    --blue: #2a4db5;
    --blue-mid: #2f63cf;
    --sky: #3fb6e8;
    --sky-soft: #63c8ef;
    --orange: #e8772b;
    --amber: #f2a13a;
    --yellow: #f6e43a;
    --white: #ffffff;
  }
  html, body {
    margin: 0;
    width: 1200px;
    height: 1200px;
    overflow: hidden;
    background: var(--page);
  }
  .stage {
    position: relative;
    width: 1200px;
    height: 1200px;
  }
  .book-cover {
    position: absolute;
    left: 242px;
    top: 60px;
    width: 718px;
    height: 1080px;
  }
  .title-word {
    font-family: "Rubik Dirt", "Impact", sans-serif;
    text-transform: uppercase;
  }
  .title-personal { fill: var(--white); }
  .title-finance { fill: var(--yellow); }
  .subtitle {
    font-family: "Barlow Condensed", "Arial Narrow", sans-serif;
    font-weight: 500;
    font-size: 33px;
    fill: var(--white);
    letter-spacing: 0.5px;
  }
  .subtitle .accent { fill: var(--yellow); font-weight: 700; }
  .audience-label {
    font-family: "Barlow Condensed", "Arial Narrow", sans-serif;
    font-weight: 700;
    font-size: 40px;
    fill: var(--navy-deep);
    letter-spacing: 0.5px;
  }
  .author-name {
    font-family: "Rubik Dirt", "Impact", sans-serif;
    fill: var(--white);
  }
</style>
</head>
<body>
<main class="stage">
  <svg class="book-cover" viewBox="0 0 718 1080" xmlns="http://www.w3.org/2000/svg" aria-label="Book cover: Personal Finance by Liam Corrado">
    <defs>
      <clipPath id="cover-clip"><rect width="718" height="1080"/></clipPath>
    </defs>
    <g clip-path="url(#cover-clip)">
      <!-- base -->
      <rect class="cover-base" width="718" height="1080" fill="var(--navy)"/>

      <!-- large orange ring behind, right side -->
      <circle class="ring-amber" cx="470" cy="500" r="330" fill="none" stroke="var(--orange)" stroke-width="70"/>

      <!-- blue disc field -->
      <circle class="disc-blue" cx="330" cy="560" r="330" fill="var(--blue)"/>

      <!-- left orange circle -->
      <circle class="disc-orange" cx="120" cy="640" r="300" fill="var(--orange)"/>
      <circle class="disc-orange-inner" cx="230" cy="600" r="240" fill="var(--blue-mid)"/>

      <!-- vertical stripes on the left -->
      <g class="stripes">
        <rect x="0" y="0" width="190" height="850" fill="var(--navy)" opacity="0.55"/>
        <rect x="10" y="0" width="8" height="850" fill="var(--sky)"/>
        <rect x="32" y="0" width="6" height="850" fill="var(--sky)"/>
        <rect x="56" y="0" width="10" height="850" fill="var(--sky-soft)" opacity="0.8"/>
        <rect x="82" y="0" width="5" height="850" fill="var(--sky)"/>
        <rect x="104" y="0" width="9" height="850" fill="var(--sky)" opacity="0.85"/>
        <rect x="130" y="0" width="6" height="850" fill="var(--sky-soft)"/>
        <rect x="152" y="0" width="8" height="850" fill="var(--sky)" opacity="0.7"/>
        <rect x="176" y="0" width="5" height="850" fill="var(--sky)"/>
      </g>

      <!-- sky ring around subtitle -->
      <circle class="ring-sky" cx="517" cy="470" r="275" fill="none" stroke="var(--sky)" stroke-width="60" opacity="0.9"/>
      <circle class="ring-core" cx="517" cy="470" r="245" fill="var(--blue)"/>

      <!-- illustration placeholders -->
      <rect class="art-bills" x="20" y="360" width="300" height="420" fill="var(--sky)" opacity="0.12" role="img" aria-label="Flying dollar bills illustration"/>
      <rect class="art-coins" x="250" y="640" width="360" height="210" fill="var(--sky-soft)" opacity="0.1" role="img" aria-label="Stacks of coins line illustration"/>

      <!-- bottom author band -->
      <rect class="author-band" x="0" y="848" width="718" height="232" fill="var(--navy-deep)"/>
      <rect class="author-band-art" x="20" y="848" width="230" height="232" fill="var(--navy)" opacity="0.6" role="img" aria-label="Faint coin stack illustration"/>

      <!-- title -->
      <text class="title-word title-personal" x="359" y="172" text-anchor="middle" font-size="150" textLength="628" lengthAdjust="spacingAndGlyphs">Personal</text>
      <text class="title-word title-finance" x="352" y="356" text-anchor="middle" font-size="200" textLength="684" lengthAdjust="spacingAndGlyphs">Finance</text>

      <!-- subtitle -->
      <g class="subtitle" text-anchor="middle">
        <text x="517" y="452">MONEY MASTERY</text>
        <text x="517" y="495">AROADMAP TO:</text>
        <text x="517" y="538"><tspan class="accent">EARNING POWER</tspan> WISE</text>
        <text x="517" y="581">SPENDING <tspan class="accent">BUGETING</tspan></text>
        <text x="517" y="624">SAVING <tspan class="accent">INVESTING</tspan></text>
      </g>

      <!-- audience pill -->
      <rect class="audience-pill" x="68" y="757" width="574" height="70" rx="12" fill="var(--yellow)"/>
      <text class="audience-label" x="355" y="806" text-anchor="middle">FOR TEENS AND YOUNG ADULTS</text>

      <!-- author -->
      <text class="author-name" x="361" y="1030" text-anchor="middle" font-size="118" textLength="622" lengthAdjust="spacingAndGlyphs">LIAM CORRADO</text>
    </g>
  </svg>
</main>
</body>
</html>
```